Pathways to Brightmoor Land Ventures

size of the ad - 8”x 10.75" plus 0.25" bleed
I would like an ad for a magazine that will stand out and make people want to read the ad.
The ad should not be crowded and people reading the ad will be able to read the text.
I would like it to be a creative and modern-day design.
the list of topics should not be the focus of the ad.
the text is attached.
If you decide to use people in the ad then please no ladies.
please note that leave over 1 inch for the bottom of the footer

```html
<!DOCTYPE html>
<html lang="en">
<head>
<meta charset="utf-8">
<title>Real Estate Course – Pathways to Brightmoor Land Ventures</title>
<link href="https://fonts.googleapis.com/css2?family=Montserrat:wght@300;400;500;600;700;800&display=swap" rel="stylesheet">
<style>
  :root {
    --stage: #5a6155;
    --paper: #ffffff;
    --ink: #2f2f2f;
    --ink-soft: #3d3d3d;
    --green: #8aa45a;
    --green-deep: #7a9450;
    --hero-dark: #1b1b1b;
    --hero-mid: #3a3c36;
    --hero-light: #727d60;
  }
  * { box-sizing: border-box; margin: 0; padding: 0; }
  html, body { width: 1200px; height: 2322px; overflow: hidden; }
  body { background: var(--stage); font-family: "Montserrat", sans-serif; position: relative; }

  .ad {
    position: absolute; left: 80px; top: 462px;
    width: 936px; height: 1258px;
    transform: scale(1.1111); transform-origin: top left;
    background: var(--paper); overflow: hidden;
    box-shadow: 0 26px 30px rgba(0,0,0,0.35);
  }
  .hero-shape { position: absolute; inset: 0; width: 936px; height: 1258px; }

  .title { position: absolute; left: 43px; top: 34px; color: #fff; line-height: 1; }
  .title__real { font-size: 64px; font-weight: 400; display: block; }
  .title__estate { font-size: 99px; font-weight: 800; display: block; margin-top: 4px; letter-spacing: -1px; }
  .title__course { font-size: 66px; font-weight: 500; display: block; margin-top: 4px; }
  .title__rule { width: 314px; height: 5px; background: var(--green); margin: 18px 0 12px; }
  .title__sub { font-size: 35px; font-weight: 600; line-height: 35px; display: block; }
  .title__sub--accent { color: var(--green); font-weight: 700; }

  .photo { position: absolute; border-radius: 50%;
    box-shadow: 0 0 0 8px var(--paper), 0 0 0 13px var(--green); }
  .photo--townhouses { left: 613px; top: 138px; width: 330px; height: 330px;
    background: linear-gradient(160deg, #c9cdd2 0%, #a7a6a4 35%, #6e4a3a 60%, #5b5550 100%); }
  .photo--villa { left: 378px; top: 343px; width: 370px; height: 370px;
    background: linear-gradient(170deg, #5d8fc4 0%, #9fc2de 25%, #e9e3c7 50%, #9fc7b8 70%, #7d6a4a 100%); }

  .tagline { position: absolute; left: 45px; top: 542px; font-size: 26px; font-weight: 700;
    line-height: 27px; color: var(--ink-soft); }

  .details { position: absolute; left: 45px; top: 675px; color: var(--ink-soft); }
  .details__place { font-size: 34px; font-weight: 600; color: var(--green); line-height: 40px; }
  .details__line { font-size: 18px; font-weight: 600; line-height: 23px; }

  .offer { position: absolute; left: 45px; top: 817px; font-size: 18px; font-weight: 600;
    line-height: 23px; color: var(--ink-soft); }
  .offer__label { margin-bottom: 5px; }

  .topics { position: absolute; left: 45px; top: 922px; }
  .topics__heading { font-size: 32px; font-weight: 600; color: var(--ink); line-height: 40px; margin-bottom: 6px; }
  .topics__heading span { color: var(--green); }
  .topics__cols { display: flex; gap: 22px; }
  .topics__list { list-style: none; }
  .topics__list li { display: flex; align-items: center; gap: 6px; font-size: 18px;
    font-weight: 500; color: var(--ink); line-height: 26px; white-space: nowrap; }
  .tick { width: 14px; height: 14px; flex: none; }

  .presenter { position: absolute; left: 636px; top: 672px; width: 292px; height: 439px;
    border-radius: 140px 140px 0 0;
    background: linear-gradient(180deg, #d9b9a0 0%, #c7a58c 18%, #5a5a5c 34%, #45464a 70%, #3a3b3f 100%); }

  .footer { position: absolute; left: 0; bottom: 0; width: 936px; height: 147px;
    background: var(--green); }
  .footer__measure { position: absolute; left: 430px; top: 28px; width: 80px; height: 90px; }
</style>
</head>
<body>
  <div class="ad">
    <svg class="hero-shape" viewBox="0 0 936 1258" aria-hidden="true">
      <defs>
        <linearGradient id="hero-fill" x1="0" y1="0" x2="1" y2="0.3">
          <stop offset="0" stop-color="#1b1b1b"/>
          <stop offset="0.45" stop-color="#3a3c36"/>
          <stop offset="1" stop-color="#727d60"/>
        </linearGradient>
      </defs>
      <circle cx="240" cy="80" r="445" fill="url(#hero-fill)"/>
      <circle cx="240" cy="80" r="462" fill="none" stroke="#8aa45a" stroke-width="6"/>
    </svg>

    <h1 class="title">
      <span class="title__real">REAL</span>
      <span class="title__estate">ESTATE</span>
      <span class="title__course">COURSE</span>
      <span class="title__rule"></span>
      <span class="title__sub">PATHWAYS TO</span>
      <span class="title__sub title__sub--accent">BRIGHTMOOR</span>
      <span class="title__sub">LAND VENTURES</span>
    </h1>

    <div class="photo photo--townhouses" role="img" aria-label="Photo of a row of historic half-timbered townhouses on a cobbled street"></div>
    <div class="photo photo--villa" role="img" aria-label="Photo of a two-storey villa with arches and potted plants"></div>

    <p class="tagline">INVESTING<br>IN KNOWLEDGE<br>IS INVESTING<br>IN OPPORTUNITIES.</p>

    <div class="details">
      <p class="details__place">Elmridge</p>
      <p class="details__line">10 -Tuesday evenings sessions</p>
      <p class="details__line">Starting Feb.28</p>
      <p class="details__line">Limited Partial Scholarships</p>
    </div>

    <div class="offer">
      <p class="offer__label">Early Bird Special</p>
      <p>For those that started or<br>would like to go into real estate</p>
    </div>

    <section class="topics">
      <h2 class="topics__heading"><span>Topics:</span> partial listing</h2>
      <div class="topics__cols">
        <ul class="topics__list">
          <li><svg class="tick" viewBox="0 0 14 14"><circle cx="7" cy="7" r="5.5" fill="none" stroke="#8aa45a" stroke-width="1.6"/><path d="M4.3 7.2l2 2 5.5-6" fill="none" stroke="#8aa45a" stroke-width="1.8"/></svg>Real estate investment strategies</li>
          <li><svg class="tick" viewBox="0 0 14 14"><circle cx="7" cy="7" r="5.5" fill="none" stroke="#8aa45a" stroke-width="1.6"/><path d="M4.3 7.2l2 2 5.5-6" fill="none" stroke="#8aa45a" stroke-width="1.8"/></svg>Due diligence</li>
          <li><svg class="tick" viewBox="0 0 14 14"><circle cx="7" cy="7" r="5.5" fill="none" stroke="#8aa45a" stroke-width="1.6"/><path d="M4.3 7.2l2 2 5.5-6" fill="none" stroke="#8aa45a" stroke-width="1.8"/></svg>Financing</li>
          <li><svg class="tick" viewBox="0 0 14 14"><circle cx="7" cy="7" r="5.5" fill="none" stroke="#8aa45a" stroke-width="1.6"/><path d="M4.3 7.2l2 2 5.5-6" fill="none" stroke="#8aa45a" stroke-width="1.8"/></svg>Underwriting</li>
          <li><svg class="tick" viewBox="0 0 14 14"><circle cx="7" cy="7" r="5.5" fill="none" stroke="#8aa45a" stroke-width="1.6"/><path d="M4.3 7.2l2 2 5.5-6" fill="none" stroke="#8aa45a" stroke-width="1.8"/></svg>Property management</li>
        </ul>
        <ul class="topics__list">
          <li><svg class="tick" viewBox="0 0 14 14"><circle cx="7" cy="7" r="5.5" fill="none" stroke="#8aa45a" stroke-width="1.6"/><path d="M4.3 7.2l2 2 5.5-6" fill="none" stroke="#8aa45a" stroke-width="1.8"/></svg>Real estate Legal basics</li>
          <li><svg class="tick" viewBox="0 0 14 14"><circle cx="7" cy="7" r="5.5" fill="none" stroke="#8aa45a" stroke-width="1.6"/><path d="M4.3 7.2l2 2 5.5-6" fill="none" stroke="#8aa45a" stroke-width="1.8"/></svg>Sourcing deals</li>
          <li><svg class="tick" viewBox="0 0 14 14"><circle cx="7" cy="7" r="5.5" fill="none" stroke="#8aa45a" stroke-width="1.6"/><path d="M4.3 7.2l2 2 5.5-6" fill="none" stroke="#8aa45a" stroke-width="1.8"/></svg>Syndication</li>
          <li><svg class="tick" viewBox="0 0 14 14"><circle cx="7" cy="7" r="5.5" fill="none" stroke="#8aa45a" stroke-width="1.6"/><path d="M4.3 7.2l2 2 5.5-6" fill="none" stroke="#8aa45a" stroke-width="1.8"/></svg>Dealing with brokers</li>
          <li><svg class="tick" viewBox="0 0 14 14"><circle cx="7" cy="7" r="5.5" fill="none" stroke="#8aa45a" stroke-width="1.6"/><path d="M4.3 7.2l2 2 5.5-6" fill="none" stroke="#8aa45a" stroke-width="1.8"/></svg>Tax fundamentals</li>
        </ul>
      </div>
    </section>

    <div class="presenter" role="img" aria-label="Photo of a smiling bearded man in a grey suit giving two thumbs up"></div>

    <footer class="footer">
      <svg class="footer__measure" viewBox="0 0 80 90" aria-label="Footer space 1.25 inches">
        <path d="M40 4v24M34 11l6-7 6 7" fill="none" stroke="#fff" stroke-width="2.5"/>
        <text x="40" y="55" fill="#fff" font-family="Montserrat, sans-serif" font-size="24" font-weight="500" text-anchor="middle">1.25”</text>
        <path d="M40 64v24M34 81l6 7 6-7" fill="none" stroke="#fff" stroke-width="2.5"/>
      </svg>
    </footer>
  </div>
</body>
</html>
```